Website Design for A Leading Live Casino Software Provider

We provide live casino software to other land based and online gaming establishments. We are a B2B provider.

```html
<!DOCTYPE html>
<html lang="en">
<head>
<meta charset="utf-8">
<title>Meridian Play Studios — About Us</title>
<link href="https://fonts.googleapis.com/css2?family=Open+Sans:wght@400;600;700;800&display=swap" rel="stylesheet">
<style>
  :root{
    --navy:#0d2a5c;
    --navy-deep:#0a1f45;
    --navy-mid:#1d3f7a;
    --ink:#1a2440;
    --muted:#5a6272;
    --page:#e6e8ee;
    --header-top:#fbfbfd;
    --header-bottom:#d9dce3;
    --white:#ffffff;
    --line:#c9cdd6;
    --red:#d11a1a;
    --pill:#e9ebf0;
  }
  *{box-sizing:border-box;margin:0;padding:0}
  html,body{width:1200px;height:1200px;overflow:hidden}
  body{position:relative;background:var(--page);font-family:"Open Sans",Arial,sans-serif;color:var(--ink)}
  .abs{position:absolute}

  .top-strip{left:0;top:0;width:1200px;height:8px;background:var(--navy-deep)}
  .site-header{left:0;top:8px;width:1200px;height:105px;background:linear-gradient(var(--header-top),var(--header-bottom));border-bottom:1px solid #c3c7cf}

  .brand{left:131px;top:30px;display:flex;align-items:center;gap:10px}
  .brand-dot{width:46px;height:46px;border-radius:50%;background:var(--navy-mid)}
  .brand-name{font-weight:800;font-size:19px;color:var(--navy);line-height:1.05;width:130px;letter-spacing:.3px}

  .lang-pill{left:957px;top:20px;width:134px;height:19px;border-radius:10px;background:var(--pill);border:1px solid #d2d5dc;font-size:9.5px;color:#334;display:flex;align-items:center;padding-left:10px;gap:6px}
  .lang-pill .tri{width:0;height:0;border-left:5px solid var(--navy);border-top:3.5px solid transparent;border-bottom:3.5px solid transparent}
  .flags{margin-left:auto;margin-right:8px;display:flex;gap:5px}
  .search-pill{left:955px;top:57px;width:141px;height:19px;border-radius:10px;background:var(--pill);border:1px solid #d2d5dc;font-size:9.5px;color:#777;display:flex;align-items:center;padding-left:10px}
  .search-pill svg{margin-left:auto;margin-right:8px}

  .main-nav{left:424px;top:93px;width:667px;height:28px;border-radius:14px 14px 0 0;background:linear-gradient(#ffffff,#e3e5ea);border:1px solid #cfd2d9;display:flex;align-items:center;padding-left:18px;gap:0}
  .main-nav a{font-size:11px;font-weight:700;color:var(--navy);text-decoration:none;padding:0 15px;white-space:nowrap}
  .main-nav a.active{background:var(--navy);color:#fff;height:34px;margin-top:-8px;display:flex;align-items:center;padding:0 24px;border-radius:4px 4px 0 0}

  .hero{left:103px;top:113px;width:994px;height:274px;background:linear-gradient(100deg,#6b2a1c 0%,#a8563a 25%,#d99c7a 45%,#c07a55 60%,#5a3a30 80%,#2b2628 100%)}
  .hero-caption{left:103px;top:167px;width:444px;height:160px;background:rgba(20,14,14,.35);padding:14px 0 0 44px;color:#fff}
  .hero-caption h2{font-size:19px;font-weight:700;margin-bottom:14px}
  .hero-caption p{font-size:10.5px;line-height:14px;width:390px}
  .hero-caption .more{display:block;font-size:10.5px;margin-top:12px;margin-left:276px}
  .slider-btn{width:22px;height:22px;border-radius:50%;background:#f3f3f3;display:flex;align-items:center;justify-content:center;box-shadow:0 1px 3px rgba(0,0,0,.4)}
  .dots{left:585px;top:361px;display:flex;gap:4px}
  .dots span{width:7px;height:7px;border-radius:50%;background:#fff}
  .dots span.on{background:#333}

  .sidebar{left:103px;top:387px;width:246px;height:722px;background:var(--white);border-right:1px dashed var(--line)}
  .content{left:349px;top:387px;width:748px;height:722px;background:#f7f8fa;box-shadow:6px 0 10px rgba(0,0,0,.08)}

  .side-head{left:103px;width:246px;height:38px;background:linear-gradient(#1b3d77,var(--navy-deep));color:#fff;font-size:13px;font-weight:600;display:flex;align-items:center;justify-content:center;border-radius:0 8px 0 0}
  .tagline{left:103px;top:437px;width:246px;text-align:center;font-size:13px;font-weight:700;color:var(--navy);line-height:17px}
  .dealer-box{left:103px;top:487px;width:246px;height:198px;border-top:2px solid #dde0e6;border-bottom:2px solid #dde0e6;background:#fff}
  .dealer-photo{left:151px;top:497px;width:145px;height:179px;background:linear-gradient(160deg,#3a2a22,#a8704a 55%,#6b4a2a);border:3px solid #f0f0f0;box-shadow:0 0 0 1px #ccc}
  .chev{font-size:15px;font-weight:700;color:#222}

  .date-pill{left:132px;top:747px;width:181px;height:20px;border-radius:10px;background:var(--navy-deep);color:#fff;font-size:9.5px;font-weight:600;display:flex;align-items:center;padding:0 12px;justify-content:space-between}
  .date-pill .d{display:flex;align-items:center;gap:5px}
  .round-arrow{width:22px;height:22px;border-radius:50%;background:#eee;border:1px solid #bbb;display:flex;align-items:center;justify-content:center}
  .news-title{left:136px;top:780px;font-size:10px;font-weight:600;color:#666}
  .read-more{left:260px;top:806px;font-size:10px;color:var(--navy);text-decoration:underline}

  .blog-item{left:103px;width:246px;height:44px;border-bottom:1px dashed var(--line);padding:6px 10px 0 20px}
  .blog-item h4{font-size:10px;font-weight:700;color:var(--navy)}
  .blog-item .meta{display:flex;justify-content:flex-end;align-items:center;gap:5px;font-size:10px;color:#333;margin-top:4px}
  .more-btn{left:240px;top:1076px;width:88px;height:19px;border-radius:10px;background:linear-gradient(#fff,#dcdee3);border:1px solid #bfc3ca;font-size:10.5px;color:#333;display:flex;align-items:center;justify-content:center}

  .about h1{position:absolute;left:376px;top:420px;font-size:20px;font-weight:700;color:var(--navy)}
  .about .rule{position:absolute;left:376px;top:456px;width:677px;height:1px;background:var(--navy-mid)}
  .about-body{left:376px;top:496px;width:679px;font-size:11.5px;font-weight:700;color:var(--navy);line-height:17.5px;text-align:justify}
  .about-body p{margin-bottom:17.5px}

  .call-bar{left:427px;top:1013px;width:584px;height:28px;border-radius:14px;background:#e6e8ed;display:flex;align-items:center;padding-left:50px;font-size:11.5px;font-weight:700;color:var(--navy)}
  .call-bar .hl{color:var(--red);margin:0 4px}
  .call-icon{left:427px;top:1008px;width:38px;height:38px;border-radius:50%;background:#dde0e6;display:flex;align-items:center;justify-content:center}

  .foot-nav{left:713px;top:1079px;width:344px;height:30px;background:var(--navy-deep);border-radius:8px 8px 0 0;color:#fff;font-size:10px;display:flex;align-items:center;padding-left:30px;gap:6px}
  .to-top{left:1107px;top:1065px;width:50px;height:26px;border-radius:4px;background:var(--navy-mid);color:#fff;font-size:8px;font-weight:700;display:flex;align-items:center;justify-content:center;gap:3px}

  .site-footer{left:0;top:1109px;width:1200px;height:78px;background:linear-gradient(#fafafa,#e4e6eb);border-top:2px solid var(--navy-deep)}
  .foot-text{left:120px;top:1134px;width:948px;font-size:9.5px;line-height:12px;color:var(--navy)}
  .copyright{left:0;top:1171px;width:1200px;text-align:center;font-size:9.5px;color:#333}
  .bottom-strip{left:0;top:1187px;width:1200px;height:13px;background:var(--navy-deep)}
</style>
</head>
<body>
  <div class="abs top-strip"></div>
  <header class="abs site-header"></header>

  <div class="abs brand">
    <span class="brand-dot"></span>
    <span class="brand-name">MERIDIAN PLAY STUDIOS</span>
  </div>

  <div class="abs lang-pill"><span class="tri"></span>Language
    <span class="flags">
      <svg width="14" height="9"><rect width="14" height="9" fill="#c60b1e"/><rect y="2.3" width="14" height="4.4" fill="#ffc400"/></svg>
      <svg width="14" height="9"><rect width="14" height="9" fill="#1f3b7a"/><rect x="5.5" width="3" height="9" fill="#fff"/><rect y="3" width="14" height="3" fill="#fff"/><rect x="6.2" width="1.6" height="9" fill="#c8102e"/><rect y="3.7" width="14" height="1.6" fill="#c8102e"/></svg>
    </span>
  </div>
  <div class="abs search-pill">| Enter a keyword
    <svg width="10" height="10" viewBox="0 0 10 10"><circle cx="4" cy="4" r="3" fill="none" stroke="#999" stroke-width="1.3"/><line x1="6.2" y1="6.2" x2="9" y2="9" stroke="#999" stroke-width="1.5"/></svg>
  </div>

  <nav class="abs main-nav">
    <a class="active">HOME</a><a>LIVE GAME</a><a>OUR SOLUTION</a><a>VIDEO</a><a>NEWS &amp; EVENTS</a><a>ABOUT US</a><a>CONTACT US</a>
  </nav>

  <div class="abs hero" role="img" aria-label="Players gathered around a live casino table, smiling"></div>
  <div class="abs hero-caption">
    <h2>Lorem Ipsum</h2>
    <p>Lorem Ipsum is simply dummy text of the printing and typesetting industry. Lorem Ipsum has been the industry's standard dummy text ever since the 1500s, when</p>
    <span class="more">learn more</span>
  </div>
  <div class="abs slider-btn" style="left:524px;top:354px"><svg width="8" height="8"><path d="M6 0L1 4L6 8z" fill="#333"/></svg></div>
  <div class="abs dots"><span></span><span class="on"></span><span></span><span></span></div>
  <div class="abs slider-btn" style="left:666px;top:354px"><svg width="8" height="8"><path d="M2 0L7 4L2 8z" fill="#333"/></svg></div>

  <aside class="abs sidebar"></aside>
  <main class="abs content"></main>

  <div class="abs side-head" style="top:388px">Get To Know our Beautiful Dealers</div>
  <div class="abs tagline">They Will Ensure Your Players<br>are Smiling Even when Losing!</div>
  <div class="abs dealer-box"></div>
  <div class="abs dealer-photo" role="img" aria-label="Portrait of a live dealer holding a playing card"></div>
  <span class="abs chev" style="left:118px;top:574px">&#8249;</span>
  <span class="abs chev" style="left:312px;top:574px">&#8250;</span>

  <div class="abs side-head" style="top:697px">News &amp; Events</div>
  <div class="abs date-pill"><span>2/9</span>
    <span class="d"><svg width="10" height="10"><circle cx="5" cy="5" r="4" fill="none" stroke="#fff" stroke-width="1.2"/><path d="M5 2.5V5H7" stroke="#fff" fill="none"/></svg>08/01/2012</span>
  </div>
  <div class="abs round-arrow" style="left:95px;top:776px"><svg width="8" height="8"><path d="M6 0L1 4L6 8z" fill="#333"/></svg></div>
  <div class="abs news-title">THE EVOLUTION OF OUR DEALERS</div>
  <div class="abs round-arrow" style="left:329px;top:776px"><svg width="8" height="8"><path d="M2 0L7 4L2 8z" fill="#333"/></svg></div>
  <div class="abs read-more">read more</div>

  <div class="abs side-head" style="top:837px">Latest Blog Article</div>
  <div class="abs blog-item" style="top:877px"><h4>THE EVOLUTION OF OUR DEALERS</h4><div class="meta"><svg width="12" height="8"><ellipse cx="6" cy="4" rx="5.5" ry="3.5" fill="none" stroke="#333"/><circle cx="6" cy="4" r="1.6" fill="#333"/></svg><svg width="10" height="10"><circle cx="5" cy="5" r="4" fill="none" stroke="#333" stroke-width="1.2"/><path d="M5 2.5V5H7" stroke="#333" fill="none"/></svg>11/02/2012</div></div>
  <div class="abs blog-item" style="top:921px"><h4>THE EVOLUTION OF OUR DEALERS</h4><div class="meta"><svg width="12" height="8"><ellipse cx="6" cy="4" rx="5.5" ry="3.5" fill="none" stroke="#333"/><circle cx="6" cy="4" r="1.6" fill="#333"/></svg><svg width="10" height="10"><circle cx="5" cy="5" r="4" fill="none" stroke="#333" stroke-width="1.2"/><path d="M5 2.5V5H7" stroke="#333" fill="none"/></svg>11/02/2012</div></div>
  <div class="abs blog-item" style="top:965px"><h4>THE EVOLUTION OF OUR DEALERS</h4><div class="meta"><svg width="12" height="8"><ellipse cx="6" cy="4" rx="5.5" ry="3.5" fill="none" stroke="#333"/><circle cx="6" cy="4" r="1.6" fill="#333"/></svg><svg width="10" height="10"><circle cx="5" cy="5" r="4" fill="none" stroke="#333" stroke-width="1.2"/><path d="M5 2.5V5H7" stroke="#333" fill="none"/></svg>11/02/2012</div></div>
  <div class="abs blog-item" style="top:1009px"><h4>THE EVOLUTION OF OUR DEALERS</h4><div class="meta"><svg width="12" height="8"><ellipse cx="6" cy="4" rx="5.5" ry="3.5" fill="none" stroke="#333"/><circle cx="6" cy="4" r="1.6" fill="#333"/></svg><svg width="10" height="10"><circle cx="5" cy="5" r="4" fill="none" stroke="#333" stroke-width="1.2"/><path d="M5 2.5V5H7" stroke="#333" fill="none"/></svg>11/02/2012</div></div>
  <div class="abs more-btn">More ...</div>

  <section class="about">
    <h1>ABOUT US</h1>
    <div class="rule"></div>
  </section>
  <div class="abs about-body">
    <p>WE ARE MERIDIAN PLAY STUDIOS S.A. THE PREEMINENT PROVIDERS OF LIVE INTERACTIVE STREAMING GAMES OF SKILL AND CHANCE.</p>
    <p>THE ONLINE GAMING INDUSTRY HAS COME A LONG WAY IN THE LAST DECADE. IN TODAY'S VERY COMPETITIVE MARKET YOU MUST PROVIDE YOUR CUSTOMERS WITH NEW AND UNIQUE GAMING VENUES. THAT'S WHERE WE COME IN.</p>
    <p>OUR SUITE OF LIVE INTERACTIVE GAMES ADDS VALUE TO YOUR EXISTING GAMING ENVIRONMENTS WITH NO EROSION OF PROFIT FROM YOUR OTHER ESTABLISHED REVENUE SOURCES. OUR PRODUCTS ARE GREAT AFFILIATE DRIVERS ... LIVE INTERACTIVE GAMING FROM MPS IS YOUR PROFIT FORCE MULTIPLIER!</p>
    <p>WE INVITE YOU PERUSE OUR DEMONSTRATION VIDEOS AND MAKE CONTACT WITH US FOR A PERSONAL EVALUATION OF HOW MPS'S GAMING SOFTWARE CAN BE PUT TO WORK FOR YOU.</p>
    <p>WE ARE MERIDIAN PLAY STUDIOS S.A. THE PREEMINENT PROVIDERS OF LIVE INTERACTIVE STREAMING GAMES OF SKILL AND CHANCE.</p>
  </div>

  <div class="abs call-bar">CALL TOLL <span class="hl">FREE</span> 1-XXX-XXX-XXXX AND GET A <span class="hl">FREE DEMO</span> OF OUR SOFTWARE AND SOLUTIONS</div>
  <div class="abs call-icon"><svg width="16" height="22" viewBox="0 0 16 22"><path d="M5 1C2 2 1 5 1 11s1 9 4 10l2-1-1-6-3 0c-.5-2-.5-4 0-6l3 0 1-6z" fill="var(--navy)"/></svg></div>

  <nav class="abs foot-nav"><span>Home</span>|<span>Live Game</span>|<span>Our Solution</span>|<span>About us</span>|<span>Contact us</span>|</nav>
  <div class="abs to-top"><svg width="6" height="5"><path d="M3 0L6 5H0z" fill="#fff"/></svg>TOP</div>

  <footer class="abs site-footer"></footer>
  <p class="abs foot-text">Meridian Play Studios is a leader among online casino software providers. Our team of expert internet casino software developers, managers and marketers are here to ensure that any project you need, is a project Meridian Play Studios can deliver. Our Casino services and consulting solutions can take your business to the next level. Our online casino software licensing can help any start up achieve the quickest and most secure return on investment.</p>
  <p class="abs copyright">all right resrved © copyright reserved</p>
  <div class="abs bottom-strip"></div>
</body>
</html>
```